Birchwell Landing - Multifamily Development

Birchwell Landing is a Luxury Multifamily Development project located in Orange, NJ. This project will be completed in three phases with the first phase about 75% complete. Each phase will have a different name as follows
CREST Birchwell Landing
RIDGE Birchwell Landing
ZENITHAL Birchwell Landing
We are going to install a banner on the side of the first building which will act as advertising for all buildings. We will eventually need advertising that will be in the windows as well as marketing materials . We want the marketing for this project to be similar for all three phases. At the moment, we are starting with this first simple banner. Attached is a rough idea of the look as well as our color palette. If you feel the color palette is a little too monochrome, feel free to propose an accent color. You can also visit our website to see more info on our company as well as the project. www.tolvarhq.com Finally, if you need AI files (ie. for the logo), we can send to you. Thanks..

```html
<!DOCTYPE html>
<html lang="en">
<head>
<meta charset="utf-8">
<title>Birchwell Landing – Vertical Banner</title>
<link rel="stylesheet" href="https://fonts.googleapis.com/css2?family=Archivo:wght@400;600;800&display=swap">
<style>
  :root {
    --navy: #1b2536;
    --slate-blue: #4a6ea3;
    --rule-grey: #a9b4c6;
    --paper: #ffffff;
    --bg-top: #e4e4e4;
    --bg-mid: #fbfbfb;
    --bg-bottom: #e9e9e9;
  }
  * { margin: 0; padding: 0; box-sizing: border-box; }
  html, body { width: 1200px; height: 1000px; overflow: hidden; }
  body {
    position: relative;
    background: linear-gradient(180deg, var(--bg-top) 0%, var(--bg-mid) 58%, var(--bg-bottom) 100%);
    font-family: "Archivo", Arial, sans-serif;
  }
  .banner { position: absolute; display: block; }
  .banner--large { left: 263px; top: 0; width: 260px; height: 1000px; }
  .banner--small { left: 771px; top: 180px; width: 167px; height: 642px; }
  .banner text { font-family: "Archivo", Arial, sans-serif; }
  .brand-name { fill: var(--navy); font-weight: 800; }
  .project-name { fill: var(--navy); font-weight: 600; letter-spacing: 3px; }
  .tagline { fill: var(--paper); font-weight: 600; }
  .phone-digit { fill: var(--paper); font-weight: 800; }
  .web-address { fill: var(--rule-grey); font-weight: 400; }
  .corner-brand {
    position: absolute; right: 22px; bottom: 28px;
    font-weight: 800; font-size: 50px; color: var(--navy); letter-spacing: 1px;
  }
</style>
</head>
<body>

<svg class="banner banner--large" viewBox="0 0 260 1000" aria-label="Birchwell Landing banner">
  <defs>
    <symbol id="banner-artwork" viewBox="0 0 260 1000">
      <!-- white header with downward chevron edge -->
      <rect x="0" y="0" width="260" height="1000" fill="var(--navy)"/>
      <polygon points="0,0 260,0 260,335 130,287 0,335" fill="var(--paper)" stroke="var(--navy)" stroke-width="2"/>

      <text class="brand-name" x="130" y="138" text-anchor="middle" font-size="56">TOLVAR</text>
      <rect x="17" y="181" width="215" height="4" fill="var(--navy)"/>
      <text class="project-name" x="130" y="230" text-anchor="middle" font-size="30">BIRCHWELL</text>
      <text class="project-name" x="130" y="272" text-anchor="middle" font-size="30">LANDING</text>

      <!-- vertical tagline -->
      <text class="tagline" transform="translate(82 625) rotate(-90)" text-anchor="middle" font-size="44">LUXURY APARTMENT</text>
      <text class="tagline" transform="translate(150 625) rotate(-90)" text-anchor="middle" font-size="44">RENTALS</text>
      <rect x="130" y="345" width="3" height="140" fill="var(--rule-grey)"/>
      <rect x="130" y="765" width="3" height="140" fill="var(--rule-grey)"/>

      <!-- phone column -->
      <rect x="170" y="345" width="57" height="560" fill="var(--slate-blue)"/>
      <g class="phone-digit" font-size="46" text-anchor="middle">
        <text x="198.5" y="387">2</text>
        <text x="198.5" y="433">0</text>
        <text x="198.5" y="479">1</text>
        <text x="198.5" y="522">-</text>
        <text x="198.5" y="571">5</text>
        <text x="198.5" y="617">5</text>
        <text x="198.5" y="663">5</text>
        <text x="198.5" y="706">-</text>
        <text x="198.5" y="755">0</text>
        <text x="198.5" y="801">1</text>
        <text x="198.5" y="847">8</text>
        <text x="198.5" y="893">7</text>
      </g>

      <rect x="22" y="935" width="215" height="3" fill="var(--rule-grey)"/>
      <text class="web-address" x="130" y="977" text-anchor="middle" font-size="27">TOLVARHQ.COM</text>
    </symbol>
  </defs>
  <use href="#banner-artwork" width="260" height="1000"/>
</svg>

<svg class="banner banner--small" viewBox="0 0 260 1000" aria-label="Birchwell Landing banner, small size">
  <use href="#banner-artwork" width="260" height="1000"/>
</svg>

<div class="corner-brand">TOLVAR</div>

</body>
</html>
```